Create Website for new Home services company

We need a website built for a new home services company we are primarily a surface refinishing company that repairs cracks in tubs and resurfaces tubs, sinks or vanities also repainting cabinets as well.

```html
<!DOCTYPE html>
<html lang="en">
<head>
<meta charset="utf-8">
<title>Hartwell Home Services</title>
<link href="https://fonts.googleapis.com/css2?family=Lora:wght@700&family=Lato:wght@400;700&display=swap" rel="stylesheet">
<style>
:root{
  --cyan:#13b5d6;
  --cyan-dark:#0a93b3;
  --ink:#1b1b1b;
  --dark:#141414;
  --text:#333;
  --muted:#777;
  --white:#fff;
  --light:#f3f3f3;
}
*{box-sizing:border-box;margin:0;padding:0}
html,body{width:1200px;height:3108px;overflow:hidden}
body{position:relative;background:var(--white);font-family:"Lato",sans-serif;color:var(--text)}
.abs{position:absolute}
.serif{font-family:"Lora",serif;font-weight:700}

/* header */
.brand{left:28px;top:14px}
.brand-name{font-family:"Lora",serif;font-weight:700;font-size:38px;color:var(--ink);line-height:1}
.brand-sub{font-family:"Lato",sans-serif;font-size:15px;letter-spacing:9px;color:var(--cyan);margin-top:6px}
.topbar{right:28px;top:10px;display:flex;gap:30px;font-size:14px;color:var(--ink);font-weight:700}
.topbar span{display:flex;align-items:center;gap:8px}
.topbar svg{width:26px;height:26px}
.nav{right:28px;top:62px;display:flex;align-items:center;gap:8px}
.nav a{font-size:18px;color:var(--ink);text-decoration:none;padding:8px 20px}
.nav a.active{background:var(--cyan);color:var(--white)}
.nav a.cta{background:var(--cyan);color:var(--white);font-weight:700;transform:skewX(-10deg);margin-left:10px;padding:8px 24px}

/* hero */
.hero-photo{left:0;top:112px;width:1200px;height:560px;background:linear-gradient(120deg,#5a4a3f 0%,#2e2a28 40%,#1e1e1e 70%,#3a3532 100%)}
.hero-box{left:222px;top:240px;width:756px;height:236px;background:rgba(19,181,214,.82);text-align:center;color:var(--white);padding-top:38px}
.hero-box h1{font-family:"Lora",serif;font-weight:700;font-size:38px;line-height:1.15}
.hero-box h1 small{display:block;font-size:38px}
.hero-box p{font-size:14px;line-height:1.5;width:520px;margin:14px auto 0}
.btn{display:inline-block;font-weight:700;font-size:20px;padding:14px 40px;transform:skewX(-10deg)}
.hero-btn{left:490px;top:480px;background:var(--white);color:var(--cyan);width:220px;text-align:center;box-shadow:0 3px 8px rgba(0,0,0,.25)}
.dots{left:570px;top:612px;display:flex;gap:10px}
.dots i{width:10px;height:10px;border-radius:50%;background:#999;display:block}
.dots i.on{background:var(--white)}

/* services */
.section-title{width:1200px;left:0;text-align:center;font-family:"Lora",serif;font-weight:700;font-size:38px;color:var(--ink)}
.section-title::after{content:"";display:block;width:36px;height:3px;background:var(--cyan);margin:10px auto 0}
.card{top:830px;width:290px}
.card .ph{height:225px;border-radius:14px 14px 0 0}
.card .label{background:var(--cyan);color:var(--white);font-family:"Lora",serif;font-weight:700;font-size:20px;text-align:center;height:72px;display:flex;align-items:center;justify-content:center;line-height:1.2;border-radius:0 0 14px 14px}
.more-btn{left:506px;top:1186px;width:188px;text-align:center;background:var(--cyan);color:var(--white);box-shadow:0 3px 8px rgba(0,0,0,.25)}

/* about */
.about-title{left:112px;top:1410px;font-family:"Lora",serif;font-weight:700;font-size:42px;color:var(--white);line-height:1.25;width:420px}
.about-title::after{content:"";display:block;width:36px;height:3px;background:var(--cyan);margin-top:10px}
.about-text{left:112px;width:420px;color:#ddd;font-size:15px;line-height:1.6}
.about-btn{left:112px;top:1790px;background:var(--white);color:var(--cyan);width:180px;text-align:center}
.about-frame{left:590px;top:1400px;width:520px;height:470px;border:4px solid var(--cyan)}
.about-photo{left:560px;top:1430px;width:520px;height:470px;background:linear-gradient(135deg,#e9e4de 0%,#cfc3b6 55%,#a89886 100%)}

/* testimonial */
.quote{left:180px;top:2110px;font-family:"Lora",serif;font-size:160px;color:#ccc;line-height:1}
.avatar{left:118px;top:2150px;width:264px;height:264px;border-radius:50%;border:6px solid var(--cyan);background:radial-gradient(circle at 50% 40%,#e8d9cc 0%,#b8cbd6 70%)}
.t-name{left:405px;top:2148px;font-size:22px;font-weight:700;color:var(--ink)}
.t-text{left:405px;width:690px;font-size:15px;line-height:1.55;color:var(--text)}
.t-thanks{left:405px;top:2320px;font-size:22px;color:var(--cyan)}
.arrow{top:2248px;width:40px;height:40px;border-radius:50%;display:flex;align-items:center;justify-content:center}

/* contact */
.form-card{left:110px;top:2420px;width:390px;height:570px;background:var(--white);border-radius:16px;box-shadow:0 6px 20px rgba(0,0,0,.25);padding:30px 24px}
.form-card h2{font-family:"Lora",serif;font-weight:700;font-size:38px;text-align:center;color:var(--ink)}
.form-card h2::after{content:"";display:block;width:36px;height:3px;background:var(--cyan);margin:8px auto 18px}
.field{border:1px solid #999;border-radius:8px;height:62px;margin:14px 0;padding:18px 14px;font-size:17px;color:var(--ink)}
.field.area{height:124px}
.submit{left:210px;top:2918px;width:190px;text-align:center;background:var(--cyan);color:var(--white);box-shadow:0 3px 8px rgba(0,0,0,.3)}
.f-brand{left:580px;top:2598px}
.f-brand .brand-name{color:var(--white);font-size:40px}
.f-text{left:580px;top:2700px;width:520px;color:#ddd;font-size:15px;line-height:1.6}
.f-item{display:flex;align-items:center;gap:12px;color:var(--white);font-size:15px;line-height:1.4}
.f-item svg{width:34px;height:34px;flex:none}
.footer{left:0;top:3060px;width:1200px;height:48px;background:var(--cyan);color:var(--white);font-size:14px;text-align:center;line-height:48px;font-weight:700}
</style>
</head>
<body>

<!-- header -->
<div class="abs brand">
  <div class="brand-name">HARTWELL HOME</div>
  <div class="brand-sub">SERVICES</div>
</div>
<div class="abs topbar">
  <span><svg viewBox="0 0 26 26"><circle cx="13" cy="13" r="13" fill="#13b5d6"/><circle cx="13" cy="13" r="7" fill="none" stroke="#fff" stroke-width="2"/><path d="M13 9v4l3 2" stroke="#fff" stroke-width="2" fill="none"/></svg>24/7 Service</span>
  <span><svg viewBox="0 0 26 26"><circle cx="13" cy="13" r="13" fill="#13b5d6"/><path d="M9 7l3 3-2 2c1 2 2 3 4 4l2-2 3 3-2 2c-5 0-10-5-10-10z" fill="#fff"/></svg>+1 555 010 2040</span>
  <span><svg viewBox="0 0 26 26"><circle cx="13" cy="13" r="13" fill="#13b5d6"/><rect x="7" y="9" width="12" height="9" fill="#fff"/><path d="M7 9l6 5 6-5" stroke="#13b5d6" stroke-width="1.5" fill="none"/></svg>info@hartwellhomeservices.com</span>
</div>
<nav class="abs nav">
  <a class="active">Home</a><a>About</a><a>Categories</a><a>Reviews</a><a class="cta">Contact Us</a>
</nav>

<!-- hero -->
<div class="abs hero-photo" role="img" aria-label="Technician refinishing a surface with a power tool"></div>
<svg class="abs" style="left:0;top:560px" width="1200" height="130" viewBox="0 0 1200 130">
  <polygon points="0,30 700,80 1200,90 1200,130 0,130" fill="#fff"/>
  <polygon points="0,30 700,80 1200,90 1200,100 700,92 0,92" fill="#13b5d6"/>
</svg>
<div class="abs hero-box">
  <h1>WELCOME TO<small>HARTWELL HOME SERVICES</small></h1>
  <p>Smooth, bright and like-new surfaces for your bathroom and kitchen. We repair, resurface and refinish tubs, sinks, vanities and cabinets with care and lasting quality.</p>
</div>
<div class="abs btn hero-btn">Get Started</div>
<div class="abs dots"><i></i><i class="on"></i><i></i><i></i></div>

<!-- services -->
<h2 class="abs section-title" style="top:728px">OUR SERVICES</h2>
<div class="abs card" style="left:112px">
  <div class="ph" role="img" aria-label="Bright bathroom with a freestanding tub" style="background:linear-gradient(160deg,#f2f0ec,#c9c3bb)"></div>
  <div class="label">REPAIRS CRACKS IN<br>TUBS</div>
</div>
<div class="abs card" style="left:455px">
  <div class="ph" role="img" aria-label="Bathroom vanity with white sink" style="background:linear-gradient(160deg,#e7e9ea,#9aa3a8)"></div>
  <div class="label">RESURFACES TUBS, SINKS<br>OR VANITIES</div>
</div>
<div class="abs card" style="left:798px">
  <div class="ph" role="img" aria-label="Workers repainting kitchen cabinets" style="background:linear-gradient(160deg,#c8a47c,#5f6f7c)"></div>
  <div class="label">REPAINTING<br>CABINETS</div>
</div>
<div class="abs btn more-btn">View More</div>

<!-- about -->
<svg class="abs" style="left:0;top:1300px" width="1200" height="680" viewBox="0 0 1200 680">
  <polygon points="0,35 1200,85 1200,600 0,660" fill="#141414"/>
  <polygon points="0,610 1200,560 1200,600 0,660" fill="#13b5d6"/>
  <polygon points="0,630 1200,585 1200,600 0,660" fill="#0a93b3"/>
</svg>
<h2 class="abs about-title">ABOUT HARTWELL HOME SERVICES</h2>
<p class="abs about-text" style="top:1556px">We are a surface refinishing team that brings tired bathrooms and kitchens back to life. From small chips to deep cracks, we restore tubs, sinks and vanities to a clean, glossy finish without costly replacement.</p>
<p class="abs about-text" style="top:1690px">Our cabinet repainting service gives your kitchen a fresh new look in days, using durable coatings and careful prep work.</p>
<div class="abs btn about-btn">Read More</div>
<div class="abs about-frame"></div>
<div class="abs about-photo" role="img" aria-label="Smiling worker carrying materials in a bright room"></div>

<!-- testimonials -->
<h2 class="abs section-title" style="top:2040px">WHAT CUSTOMER SAYS</h2>
<div class="abs quote">&ldquo;</div>
<div class="abs avatar" role="img" aria-label="Portrait of a happy customer"></div>
<div class="abs t-name">Dana Whitfield</div>
<p class="abs t-text" style="top:2184px">The team repaired a long crack in our tub and refinished it so well it looks brand new. They were on time, tidy and friendly from start to finish.</p>
<p class="abs t-text" style="top:2258px">Our old vanity looks modern again. Great price, quick work and a finish that still shines months later.</p>
<div class="abs t-thanks">Thanks, Hartwell Home Services.</div>
<div class="abs arrow" style="left:32px;background:#bbb"><svg width="16" height="16" viewBox="0 0 16 16"><path d="M11 2L5 8l6 6" stroke="#fff" stroke-width="3" fill="none"/></svg></div>
<div class="abs arrow" style="left:1128px;background:#111"><svg width="16" height="16" viewBox="0 0 16 16"><path d="M5 2l6 6-6 6" stroke="#fff" stroke-width="3" fill="none"/></svg></div>

<!-- contact -->
<svg class="abs" style="left:0;top:2400px" width="1200" height="660" viewBox="0 0 1200 660">
  <polygon points="0,60 1200,0 1200,660 0,660" fill="#f3f3f3"/>
  <polygon points="0,150 1200,20 1200,660 0,660" fill="#141414"/>
  <polygon points="0,600 1200,640 1200,660 0,660" fill="#fff"/>
</svg>
<div class="abs form-card">
  <h2>CONTACT US</h2>
  <div class="field">Name</div>
  <div class="field">Email</div>
  <div class="field">Phone Number</div>
  <div class="field area">Message</div>
</div>
<div class="abs btn submit">Submit</div>

<div class="abs f-brand">
  <div class="brand-name">HARTWELL HOME</div>
  <div class="brand-sub">SERVICES</div>
</div>
<p class="abs f-text">Refinishing tubs, sinks, vanities and cabinets across the area. Fast scheduling, clean work and finishes built to last, backed by friendly service from first call to final walkthrough.</p>
<div class="abs f-item" style="left:580px;top:2852px">
  <svg viewBox="0 0 34 34"><circle cx="17" cy="17" r="17" fill="#fff"/><path d="M17 8a6 6 0 0 0-6 6c0 5 6 12 6 12s6-7 6-12a6 6 0 0 0-6-6z" fill="#141414"/><circle cx="17" cy="14" r="2.2" fill="#fff"/></svg>
  <span>Hartwell Home Services<br>United States</span>
</div>
<div class="abs f-item" style="left:880px;top:2852px">
  <svg viewBox="0 0 34 34"><circle cx="17" cy="17" r="17" fill="#fff"/><path d="M12 9l4 4-2.5 2.5c1.3 2.5 2.5 3.7 5 5L21 18l4 4-2.5 2.5C16 24.5 9.5 18 9.5 11.5z" fill="#141414"/></svg>
  <span>+1 555 010 2040</span>
</div>
<div class="abs f-item" style="left:580px;top:2920px">
  <svg viewBox="0 0 34 34"><circle cx="17" cy="17" r="17" fill="#fff"/><rect x="9" y="11" width="16" height="12" fill="#141414"/><path d="M9 11l8 6 8-6" stroke="#fff" stroke-width="1.5" fill="none"/></svg>
  <span>info@hartwellhomeservices.com</span>
</div>

<div class="abs footer">Copyright&copy;2021 Hartwell Home Services.All Rights Reserved</div>

</body>
</html>
```